Business Card - I already have a Logo

I have a logo, I just want a business card designed that uses it. I would like to see designs that are very clean, have a sense of health and wellbeing, up-market clientele.

Target Market(s)

People interested in health and well-being, people with money! Ages 25-70

Industry/Entity Type

Massage Therapy

Contact Information for Business Card

Tove Brinck
Integrative Bodyworker

KaHuna, Remedial, Pregnancy & Maya Abdominal Massage, Body Based Psychology. Health fund rebates available
0437615290
info@wrenmossvale.com.au

Colors
86cfc6
33b8a4
00a990
85cae6
cee9f5
33a6d7
85acd3
3276b5
0355a3

Requirements
Must have
• Clean, simple, elegant design, using my existing logo

```html
<!DOCTYPE html>
<html lang="en">
<head>
<meta charset="utf-8">
<title>Wren Mossvale Massage – Business Card</title>
<link rel="stylesheet" href="https://fonts.googleapis.com/css2?family=Questrial&display=swap">
<style>
  :root {
    --backdrop: #7a8496;
    --card: #ffffff;
    --card-tint: #f1f5f7;
    --aqua: #86cfc6;
    --teal: #33b8a4;
    --sky: #85cae6;
    --ice: #cee9f5;
    --blue: #33a6d7;
    --navy: #3276b5;
    --ink: #3a3f45;
    --ink-soft: #6b7178;
  }
  * { box-sizing: border-box; margin: 0; padding: 0; }
  html, body { width: 1200px; height: 809px; overflow: hidden; }
  body {
    background: var(--backdrop);
    font-family: "Questrial", "Century Gothic", sans-serif;
    display: flex;
    align-items: center;
    justify-content: center;
    gap: 60px;
  }
  .card {
    position: relative;
    width: 520px;
    height: 300px;
    background: var(--card);
    overflow: hidden;
  }

  /* Back: contact details */
  .card-back { display: flex; }
  .brand-panel {
    width: 190px;
    display: flex;
    flex-direction: column;
    align-items: center;
    justify-content: center;
    gap: 12px;
    border-right: 1.5px solid var(--blue);
  }
  .brand-dot {
    width: 46px; height: 46px;
    border-radius: 50%;
    background: var(--aqua);
  }
  .brand-name {
    color: var(--teal);
    font-size: 20px;
    line-height: 1.15;
    text-align: center;
  }
  .details { flex: 1; display: flex; flex-direction: column; }
  .person { padding: 30px 24px 18px; }
  .person-name { font-size: 26px; color: var(--ink); font-weight: 700; letter-spacing: .5px; }
  .person-role { font-size: 14px; color: var(--ink-soft); margin-top: 4px; }
  .contact-list { list-style: none; flex: 1; display: flex; flex-direction: column; }
  .contact-row {
    flex: 1;
    display: flex;
    align-items: center;
    gap: 14px;
    padding-left: 14px;
    border-top: 1px solid var(--sky);
    font-size: 14px;
    color: var(--ink);
    position: relative;
  }
  .contact-row::after {
    content: "";
    position: absolute;
    right: 0; top: 0; bottom: 0;
    width: 22px;
    background: linear-gradient(180deg, var(--sky), var(--blue));
  }
  .contact-row:nth-child(2)::after { background: linear-gradient(180deg, var(--aqua), var(--teal)); }
  .contact-row:nth-child(3)::after { background: linear-gradient(180deg, var(--blue), var(--navy)); }
  .contact-icon { width: 18px; height: 18px; flex: none; }

  /* Front: brand */
  .card-front {
    background: radial-gradient(circle at 55% 50%, var(--card) 0%, var(--card-tint) 60%, var(--ice) 140%);
    display: flex;
    align-items: center;
    justify-content: center;
    gap: 18px;
  }
  .card-front::before {
    content: "";
    position: absolute;
    left: 0; right: 0; bottom: 0;
    height: 10px;
    background: linear-gradient(90deg, var(--teal), var(--blue));
  }
  .card-front .brand-dot { width: 70px; height: 70px; }
  .card-front .brand-name { font-size: 30px; text-align: left; }
</style>
</head>
<body>
  <section class="card card-back" aria-label="Business card back">
    <div class="brand-panel">
      <span class="brand-dot"></span>
      <p class="brand-name">Wren Mossvale<br>Massage</p>
    </div>
    <div class="details">
      <div class="person">
        <h1 class="person-name">Tove Brinck</h1>
        <p class="person-role">Integrative Bodyworker</p>
      </div>
      <ul class="contact-list">
        <li class="contact-row">
          <svg class="contact-icon" viewBox="0 0 18 18"><circle cx="9" cy="9" r="8.5" fill="var(--blue)"/><rect x="6" y="4" width="6" height="10" rx="1.2" fill="none" stroke="#fff" stroke-width="1.3"/></svg>
          0437615290
        </li>
        <li class="contact-row">
          <svg class="contact-icon" viewBox="0 0 18 18"><circle cx="9" cy="9" r="8.5" fill="var(--blue)"/><rect x="4.5" y="5.5" width="9" height="7" fill="none" stroke="#fff" stroke-width="1.2"/><path d="M4.5 5.5 9 9.5l4.5-4" fill="none" stroke="#fff" stroke-width="1.2"/></svg>
          info@wrenmossvale.com.au
        </li>
        <li class="contact-row">
          <svg class="contact-icon" viewBox="0 0 18 18"><circle cx="9" cy="9" r="8.5" fill="var(--blue)"/><circle cx="9" cy="9" r="4.5" fill="none" stroke="#fff" stroke-width="1.2"/><path d="M4.5 9h9M9 4.5c-2 2.5-2 6.5 0 9M9 4.5c2 2.5 2 6.5 0 9" fill="none" stroke="#fff" stroke-width="1"/></svg>
          www.wrenmossvale.com
        </li>
      </ul>
    </div>
  </section>

  <section class="card card-front" aria-label="Business card front">
    <span class="brand-dot"></span>
    <p class="brand-name">Wren Mossvale<br>Massage</p>
  </section>
</body>
</html>
```